This book will apply the 12 Steps to gaming addiction, also known as video game addiction. The primary purpose of the book is to provide an effective solution for this new type of addiction. The solution is based on the rich and successful concepts of traditional twelve-step programs like RL.

The title on the cover will be "Nine Doors Past the Glowing Screen" and "by Martin Quorby". A subtitle can be used if it works in your design of "A Practical Path Beyond Compulsive Console Play". Cover will be for a 6" x 9" book approximately 110 pages in length.

Some back cover text including some review quotes and an author bio are in the attached Word doc. There is also an author photo attached for for the back cover.

Requirements
Must have
• For the cover design it could be stylized, or an image, a partial image, or whatever. I am open to suggestions. Think about what would be noticed by a person searching for help with moderating their video game use, or by the parents or loved ones of problem gamers. Something contemporary and eye catching.

```html
<!DOCTYPE html>
<html lang="en">
<head>
<meta charset="utf-8">
<title>Nine Doors Past the Glowing Screen — Cover</title>
<link rel="stylesheet" href="https://fonts.googleapis.com/css2?family=Archivo+Black&family=Silkscreen:wght@400;700&family=Pixelify+Sans:wght@600&family=Libre+Franklin:ital,wght@0,500;0,800;1,500;1,800&display=swap">
<style>
  :root {
    --page: #ffffff;
    --yellow: #f9e908;
    --red: #c8100f;
    --black: #000000;
    --white: #ffffff;
  }
  * { box-sizing: border-box; margin: 0; padding: 0; }
  html, body { width: 1200px; height: 1001px; overflow: hidden; background: var(--page); }
  .canvas { position: relative; width: 1200px; height: 1001px; }

  .front-cover {
    position: absolute; left: 76px; top: 119px; width: 509px; height: 764px;
    background: var(--yellow); overflow: hidden; text-align: center; color: var(--black);
  }
  .title-main {
    position: absolute; top: 46px; left: 0; width: 100%;
    font-family: "Archivo Black", sans-serif; font-size: 60px; line-height: 1; letter-spacing: -1px;
  }
  .title-main .accent { color: var(--red); }
  .title-pixel {
    position: absolute; top: 130px; left: 0; width: 100%;
    font-family: "Silkscreen", sans-serif; font-weight: 700; font-size: 30px; line-height: 38px;
  }
  .title-pixel .accent { color: var(--red); }
  .subtitle {
    position: absolute; top: 305px; left: 0; width: 100%;
    font-family: "Pixelify Sans", sans-serif; font-weight: 600; font-size: 21px; line-height: 29px; letter-spacing: 1px;
  }
  .cover-art {
    position: absolute; left: 77px; top: 438px; width: 354px; height: 326px;
    background: linear-gradient(180deg, #1a1a1a 0%, #000 45%, #8a0c0b 70%, #000 100%);
    clip-path: polygon(20% 0, 80% 0, 100% 100%, 0 100%);
  }
  .byline {
    position: absolute; top: 720px; left: 0; width: 100%;
    font-family: "Libre Franklin", sans-serif; font-weight: 800; font-size: 22px; letter-spacing: -0.5px;
  }
  .byline span { background: var(--yellow); padding: 2px 8px; }

  .back-cover {
    position: absolute; left: 618px; top: 119px; width: 509px; height: 764px;
    background: var(--black); color: var(--white);
    font-family: "Libre Franklin", sans-serif;
  }
  .section-heading {
    position: absolute; left: 0; width: 100%; text-align: center;
    color: var(--yellow); font-weight: 800; font-size: 13px; letter-spacing: -0.1px;
  }
  .praise-heading { top: 71px; }
  .author-heading { top: 478px; font-size: 13.5px; }
  .reviews { position: absolute; left: 75px; top: 111px; width: 360px; text-align: center; }
  .review { font-size: 10.6px; line-height: 16.5px; font-weight: 500; margin-bottom: 16.5px; }
  .review cite { display: block; font-style: italic; }
  .review cite b { font-weight: 800; }
  .author-photo {
    position: absolute; left: 69px; top: 521px; width: 142px; height: 158px;
    background: linear-gradient(160deg, #6f8a4e 0%, #3d4f2c 45%, #1b2338 100%);
  }
  .author-bio {
    position: absolute; left: 226px; top: 517px; width: 218px;
    font-size: 10.6px; line-height: 16.5px; font-weight: 500;
  }
  .author-bio i { font-style: italic; }
</style>
</head>
<body>
<div class="canvas">
  <section class="front-cover">
    <h1 class="title-main"><span class="accent">NINE</span> DOORS</h1>
    <p class="title-pixel">PAST THE<br>GLOWING<br><span class="accent">SCREEN</span></p>
    <p class="subtitle">A Practical Path Beyond<br>Compulsive Console Play</p>
    <div class="cover-art" role="img" aria-label="Illustration of black hands gripping a red game controller, wrists bound by its tangled red cable"></div>
    <p class="byline"><span>by MARTIN QUORBY</span></p>
  </section>

  <section class="back-cover">
    <h2 class="section-heading praise-heading">PRAISE FOR NINE DOORS PAST THE GLOWING SCREEN</h2>
    <div class="reviews">
      <blockquote class="review">“A must-read for anyone who is addicted to or thinks they may have a problem with digital gaming. This eloquent work will also be useful to academics and clinicians exploring potential solutions. The author recognizes the similarities between gaming addiction and other addictions, and logically applies one of the most effective known solutions for addiction - The Twelve Steps.”
        <cite>- <b>Dale Brennick</b>, Noted Interventionist and Keynote Speaker</cite></blockquote>
      <blockquote class="review">“If you suffer from digital gaming addiction, I strongly encourage you to use this book as your road map to get you back to the real world.”
        <cite>- <b>Owen Castellar</b>, Founder of Signal Current Weekly.</cite></blockquote>
      <blockquote class="review">“As a high school teacher for 24 years, husband, father, coach, and 12-Step member, I can assure you that this book will transform the life of anyone who is addicted to video games. Well written, easy to understand, and a wonderful book that will provide you with a clear road map to recovery and this includes teenagers, a group I have been working with in the classroom for decades.”
        <cite>- <b>Reuben Alvaro</b>, Harbor Vale, CA High School Teacher.</cite></blockquote>
    </div>
    <h2 class="section-heading author-heading">ABOUT THE AUTHOR</h2>
    <div class="author-photo" role="img" aria-label="Author portrait photograph"></div>
    <p class="author-bio">Marty Quorby is a Technology Consultant and Writer with many years of professional coding and consulting experience. He also struggled with addiction to drugs and alcohol and is now clean and sober in a Twelve-Step program for over 17 years. This unique combination of 12-Step experience and technology expertise led him to create <i>Nine Doors Past the Glowing Screen.</i></p>
  </section>
</div>
</body>
</html>
```